Trash/recycling can & dumpster cleaning service

We power wash the inside and outside of trash/recycling cans & dumpsters. The water is collected and disposed of properly. We use environmentally safe products that leave your bins looking and smelling new.

Target Market(s)

Homeowners/renters, HOA's, Restaurant/Bars, Grocery stores, Hotel & Motels, Vacation homes, and neighborhoods with special rules to be allowed to live there.

Industry/Entity Type

Cleaning Service

Contact Information for Business Card

Brisk Bright Bins, Lyle Brennard-president-(608)517-4036, Martin Delacour-Vice President/treasurer-(608)862-1473, Carrow Falls, WI

Font styles to use
Serif

Requirements
Nice to have
• A picture of trash can (real or animated). The colors we would like to use is the same as the picture of Varo shoes in my images, sketches, or document section. Main color the aqua blue w/the bright fluorescent yellow and orange as accent colors.

```html
<!DOCTYPE html>
<html lang="en">
<head>
<meta charset="utf-8">
<title>Brisk Bright Bins – Business Card</title>
<link rel="stylesheet" href="https://fonts.googleapis.com/css2?family=Montserrat:wght@300;400;600;700&display=swap">
<style>
  :root {
    --page: #ecebe8;
    --aqua-light: #2cc0ea;
    --aqua: #1aa4e0;
    --aqua-deep: #1489cf;
    --yellow: #f7c32a;
    --cream-light: #fff3a8;
    --cream: #fbdc6a;
    --orange: #f7941d;
    --red: #e8302b;
    --white: #ffffff;
    --ink: #1c1c1c;
    --silver-light: #e6e9ec;
    --silver: #9ea4aa;
  }
  * { box-sizing: border-box; margin: 0; padding: 0; }
  html, body { width: 1200px; height: 1000px; overflow: hidden; }
  body {
    background: var(--page);
    font-family: "Montserrat", Arial, sans-serif;
    position: relative;
  }
  .card {
    position: absolute;
    left: 220px;
    width: 760px;
    height: 434px;
    border-radius: 34px;
    overflow: hidden;
    box-shadow: 0 10px 24px rgba(0,0,0,0.18);
    background: radial-gradient(ellipse at 50% 45%, var(--aqua-light) 0%, var(--aqua) 45%, var(--aqua-deep) 100%);
  }
  .card--back { top: 40px; }
  .card--front { top: 526px; }

  .wordmark {
    font-family: "Montserrat", Arial, sans-serif;
    font-weight: 700;
    color: var(--yellow);
    text-transform: uppercase;
    letter-spacing: 2px;
    white-space: nowrap;
  }
  .card--back .wordmark {
    position: absolute;
    left: 0; right: 0; top: 185px;
    text-align: center;
    font-size: 50px;
  }

  .front-shape { position: absolute; inset: 0; width: 100%; height: 100%; }

  .card--front .wordmark {
    position: absolute;
    left: 50px; top: 50px;
    font-size: 40px;
  }
  .trash-can {
    position: absolute;
    left: 570px; top: 110px;
    width: 150px; height: 150px;
    border-radius: 10px 10px 18px 18px;
    background: linear-gradient(90deg, var(--silver) 0%, var(--silver-light) 45%, var(--silver) 100%);
  }
  .person {
    position: absolute;
    left: 50px; top: 145px;
    color: var(--white);
  }
  .person__name { font-weight: 700; font-size: 30px; line-height: 1.15; }
  .person__role { font-weight: 300; font-size: 28px; line-height: 1.15; }

  .contact {
    position: absolute;
    left: 150px; top: 318px;
    list-style: none;
    color: var(--ink);
  }
  .contact__item {
    display: flex; align-items: center; gap: 12px;
    font-size: 30px; font-weight: 400;
    line-height: 1.2;
    margin-bottom: 10px;
  }
  .contact__icon { width: 32px; height: 32px; flex: none; }
</style>
</head>
<body>
  <section class="card card--back" aria-label="Card back">
    <p class="wordmark">Brisk Bright Bins</p>
  </section>

  <section class="card card--front" aria-label="Card front">
    <svg class="front-shape" viewBox="0 0 760 434" preserveAspectRatio="none" aria-hidden="true">
      <defs>
        <linearGradient id="cream-fill" x1="0" y1="0" x2="1" y2="1">
          <stop offset="0" stop-color="var(--cream)"/>
          <stop offset="0.5" stop-color="var(--cream-light)"/>
          <stop offset="1" stop-color="var(--cream)"/>
        </linearGradient>
        <linearGradient id="edge-line" x1="0" y1="0" x2="1" y2="0">
          <stop offset="0" stop-color="var(--red)"/>
          <stop offset="1" stop-color="var(--orange)"/>
        </linearGradient>
      </defs>
      <polygon points="0,300 540,200 625,270 760,235 760,434 0,434" fill="url(#cream-fill)"/>
      <polyline points="0,300 540,200 625,270 760,235" fill="none" stroke="url(#edge-line)" stroke-width="6"/>
    </svg>

    <p class="wordmark">Brisk Bright Bins</p>
    <div class="trash-can" role="img" aria-label="Illustration of a shiny metal trash can"></div>

    <div class="person">
      <p class="person__name">Lyle Brennard</p>
      <p class="person__role">president</p>
    </div>

    <ul class="contact">
      <li class="contact__item">
        <svg class="contact__icon" viewBox="0 0 32 32" aria-hidden="true">
          <circle cx="16" cy="16" r="15" fill="var(--aqua)" stroke="var(--white)" stroke-width="1.5"/>
          <rect x="11" y="7" width="10" height="18" rx="2" fill="none" stroke="var(--white)" stroke-width="1.8"/>
          <rect x="13" y="10" width="6" height="8" fill="var(--white)"/>
          <circle cx="16" cy="21.5" r="1.2" fill="var(--white)"/>
        </svg>
        <span>(608)517-4036</span>
      </li>
      <li class="contact__item">
        <svg class="contact__icon" viewBox="0 0 32 32" aria-hidden="true">
          <circle cx="16" cy="16" r="15" fill="var(--aqua)" stroke="var(--white)" stroke-width="1.5"/>
          <path d="M16 25 C11 18 10 16 10 13 A6 6 0 0 1 22 13 C22 16 21 18 16 25 Z" fill="var(--white)"/>
          <circle cx="16" cy="13" r="2.3" fill="var(--aqua)"/>
        </svg>
        <span>Carrow Falls, WI</span>
      </li>
    </ul>
  </section>
</body>
</html>
```